BrightFern Web Design Project

BrightFern IT solutions, a IT mananaged services company is looking to redesign current website (brightfernsolutions.example).

The website should convey professionalism within the managed it services community. The layout should invite users to explore other areas of the site. Should contain tools and other current information that clients or potential clients would find useful. Product pages, special offers and informational pages should be easily editable by non-programmers. Tidewarden.example is a good site to review as an example of the design components we like.

Target Market(s)

Professional services companies with 10-100 users

Industry/Entity Type

It Company

Requirements
Must have
• • Clickable icons and graphics are good
• SEO - Wordpress could be a great platform for us to work from as we already have internal experience with it and it’s easy to update. If not Wordpress, we would need something that is easy to SEO optimize
• An “our team” section with pictures
• Sell the message to potential clients why they need managed services
• Home page needs to convey our core services at a glance
• Home page needs to load quickly
• Screenshots of our monitoring and security reports
• Easy for us to update/edit certain areas
o New products
o Testimonials
Nice to have
• • Something like TW’s savings calculator - http://www.tidewarden.example/it-savings-calculator/
• Webform to enter service ticket requests
• Motion of home page banner
• Maybe pull in RSS feeds from current tech news sources
• Rotating content on all pages to keep it fresh
• “Fern-up” feature for monthly promos
Should not have
• • Should not be overly "techie" in feel.
• Not overly wordy (like current site)

```html
<!DOCTYPE html>
<html lang="en">
<head>
<meta charset="utf-8">
<title>BrightFern IT Solutions</title>
<link href="https://fonts.googleapis.com/css2?family=Ubuntu:wght@400;500&family=Arimo:wght@400;700&display=swap" rel="stylesheet">
<style>
:root{
  --bar:#5b5b5b;
  --page:#e6e7e2;
  --header:#eeefeb;
  --green:#4cb034;
  --green-dark:#2f7d12;
  --orange:#ff6c00;
  --teal:#35a89a;
  --gray-tab:#5f5f5f;
  --text:#555;
  --ink:#222;
  --white:#fff;
  --sky-a:#1aa3dc;
  --sky-b:#7fd0f0;
}
*{box-sizing:border-box;margin:0;padding:0}
html,body{width:1200px;height:984px;overflow:hidden}
body{background:var(--page);font-family:"Arimo",Arial,sans-serif;color:var(--text);position:relative}
.topbar{position:absolute;left:0;top:0;width:1200px;height:31px;background:var(--bar);color:var(--white)}
.call{position:absolute;left:138px;top:6px;font-family:"Ubuntu",sans-serif;font-size:14px}
.call strong{font-size:18px;font-weight:500;margin-right:4px}
.call .sep{margin:0 12px}
.quick-links{position:absolute;right:163px;top:10px;font-size:11px;display:flex;gap:12px}
.header{position:absolute;left:0;top:31px;width:1200px;height:131px;background:var(--header)}
.brand{position:absolute;left:140px;top:28px;display:flex;align-items:center;gap:10px}
.brand .dot{width:74px;height:74px;border-radius:50%;background:var(--green)}
.brand .name{font-family:"Ubuntu",sans-serif;font-size:26px;font-weight:500;color:var(--green)}
.nav{position:absolute;left:437px;top:62px;display:flex;gap:31px;font-family:"Ubuntu",sans-serif;font-size:19px;color:var(--ink)}
.nav a{color:inherit;text-decoration:none;padding-bottom:8px}
.nav a.active{color:var(--green);border-bottom:3px solid var(--green)}
.tab{position:absolute;color:var(--white);font-family:"Ubuntu",sans-serif;font-weight:500}
.tab::after{content:"";position:absolute;left:var(--notch,128px);bottom:-10px;border-left:11px solid var(--c);border-bottom:10px solid transparent}
.banner{position:absolute;left:140px;top:206px;width:894px;height:248px;background:var(--white);padding:3px}
.banner .sky{width:100%;height:100%;background:linear-gradient(100deg,var(--sky-a) 0%,#2ab2e6 55%,var(--sky-b) 100%);position:relative}
.banner .photo{position:absolute;right:0;top:0;width:400px;height:100%;background:radial-gradient(ellipse at 40% 45%,#bfe6f6 0%,rgba(127,208,240,0) 70%)}
.banner p{position:absolute;left:33px;top:80px;color:var(--white);font-size:22px;line-height:26px;text-shadow:0 1px 2px rgba(0,0,0,.35)}
.home-tab{left:126px;top:190px;width:190px;height:40px;background:var(--green);--c:var(--green);font-size:32px;padding:0 0 0 46px;line-height:40px}
.panel{position:absolute;background:var(--white)}
.about{left:140px;top:505px;width:433px;height:231px;padding:52px 13px 0 11px}
.about h2{font-family:"Ubuntu",sans-serif;font-weight:400;font-size:19.5px;line-height:23px;color:var(--green-dark);margin:0 0 6px 3px}
.about p{font-size:12.4px;line-height:16.3px;letter-spacing:.2px}
.about-tab{left:126px;top:486px;width:422px;height:40px;background:var(--orange);--c:var(--orange);font-size:27px;line-height:40px;padding-left:69px}
.testimonial{left:599px;top:505px;width:435px;height:230px;padding:44px 26px 0 26px}
.testimonial p{font-size:12.4px;line-height:16.8px}
.testimonial .who{margin-top:10px;font-size:14px;color:#444;padding-left:2px}
.testimonial-tab{left:620px;top:485px;width:213px;height:41px;background:var(--teal);--c:var(--teal);font-size:27px;line-height:44px;padding-left:28px;--notch:128px}
.read-btn{position:absolute;left:238px;top:176px;width:142px;height:28px;background:var(--gray-tab);color:var(--white);font-family:"Ubuntu",sans-serif;font-weight:500;font-size:14px;line-height:28px;padding-left:25px}
.read-btn::after{content:"";position:absolute;right:-9px;top:0;border-left:9px solid var(--gray-tab);border-top:14px solid transparent;border-bottom:14px solid transparent}
.service{position:absolute;top:772px;width:219px;height:156px;background:linear-gradient(#fff 0%,#fff 45%,#f1f1f0 100%);border:1px solid #dcdcda;padding:0 8px}
.service h3{position:absolute;top:-8px;left:8px;height:25px;line-height:25px;color:var(--white);font-weight:400;font-size:15px;text-align:center;width:199px}
.service p{margin-top:33px;font-size:11.2px;line-height:13.6px}
.service .more{position:absolute;left:8px;bottom:26px;font-size:12px;font-weight:700;color:#555;letter-spacing:.4px}
.s1{left:141px}.s1 h3{background:var(--teal)}
.s2{left:366px}.s2 h3{background:var(--gray-tab);left:8px}
.s3{left:591px}.s3 h3{background:var(--green)}
.s4{left:816px}.s4 h3{background:var(--orange)}
.footer{position:absolute;left:0;top:948px;width:1200px;border-top:1px solid #cfd0cb;text-align:center;font-size:13px;color:#777;padding-top:10px}
</style>
</head>
<body>
<div class="topbar">
  <div class="call"><strong>Call us Now:</strong> (555) 014-2290<span class="sep">|</span>(555) 017-3861</div>
  <nav class="quick-links"><span>IT Consulting</span><span>|</span><span>IT Programs</span><span>|</span><span>IT Security</span><span>|</span><span>Data Backup</span></nav>
</div>
<header class="header">
  <div class="brand"><span class="dot"></span><span class="name">BrightFern</span></div>
  <nav class="nav"><a class="active">Home</a><a>Solutions</a><a>Careers</a><a>SiteMap</a><a>About us</a><a>Contact us</a></nav>
</header>

<section class="banner">
  <div class="sky">
    <div class="photo" role="img" aria-label="Photo of a businessman reaching toward the viewer holding a large metallic at-sign against a blue sky"></div>
    <p>Every Company Needs To Grow To Survive.<br>We Make Sure Your Technology<br>Is Ready For That Growth When You are</p>
  </div>
</section>
<div class="tab home-tab">Home</div>

<section class="panel about">
  <h2>BrightFern can help your business harness the power of new technology, making your business fast and efficient.</h2>
  <p>In the information age of today, one must stay abreast of current technology in order to thrive. New advancements are made daily in dispersing information and collaborative computing. High-speed networks aid in the exchange of electronic information between businesses, their customers, vendors, and peers. Businesses that are quick to act and effectively implement this technology will rise to the top.</p>
</section>
<div class="tab about-tab">brightFern IT Solution</div>

<section class="panel testimonial">
  <p>In the information age of today, one must stay abreast of current technology in order to thrive. New advancements are made daily in dispersing information and collaborative computing.In the information age of today, one must stay abreast of current technology in order to thrive.</p>
  <p class="who">Mr.Dale Orwin, Keystone Partners</p>
  <a class="read-btn">Read more</a>
</section>
<div class="tab testimonial-tab">Testimonial</div>

<article class="service s1"><h3>IT Consulting</h3><p>Insure that your existing system receives quality service. BrightFern will troubleshoot problems, install new software or parts, and keep your system in optimal condition...</p><span class="more">Read More</span></article>
<article class="service s2"><h3>IT Service Programs</h3><p>The certified professionals at BrightFern will even set up remote access for staff who work outside of the office, but need access to information at their offices...</p><span class="more">Read More</span></article>
<article class="service s3"><h3>Security Vulnerability Scan</h3><p>Assessment services provide critical information about your system hardware and software....</p><span class="more">Read More</span></article>
<article class="service s4"><h3>Data Backup and Recovery</h3><p>Standalone systems, workstations, network servers, notebooks, peripherals, replacement parts, upgrades, software, Network Design &amp; Installation -</p><span class="more">Read More</span></article>

<footer class="footer">Copyright © 2012 BrightFern.</footer>
</body>
</html>
```